Brickwise Returns Online Redesign

The company needs a new online presence built that better represents who we are and what we do. Our online presence needs to be optimised for both PC, tablet and Phone usage.

Our existing site; www.brickwisereturns.com.au - this page currently forwards to one of our sales pages.
The entire site needs to be redesigned along with the sales pages /workshop and /faststart

Here are our competition:
https://www.celiamarwood.com/
http://quorvineacademy.com.au/learning-team/celia-marwood/
http://rosalindhetheridge.com.au/
www.makeoverventures.com.au/
http://bestlayoutsplaybook.com.au/

Target Market(s)

40-55 Husband and Wife with children that are busy profesionals with a family income of 150-300k PA with 2-3 kids

Industry/Entity Type

Education

Number of Pages Required

5+ page

Font styles to use
Sans Serif
Script

Colors

Designer to choose colors to be used in the design.

Requirements
Must have
• Main Page
• Events Page
• Media Page
• Past Projects
• Blog - plesae design a template blog; both individual blogs and library (i like this http://wexo.blog/)
• eBooks page
• Shopping Cart - buy eBooks, eBook Packs and courses
• eBook download page for each eBook
• Testimonials
• Event Sales Page
• 2 hr Event - currently www.brickwisereturns.com.au/workshop & /faststart & /faststartv
Nice to have
• A few different options for sales landing pages to sell the 2 hr event
• A few different blog templates - video, text, infographic etc
• The business is a Property Educatiom, Mentoring and Consulting Company
Should not have
• This is not a real estate sales business

```html
<!DOCTYPE html>
<html lang="en">
<head>
<meta charset="utf-8">
<title>Brickwise Returns – Renovating Property for Profits Workshop</title>
<link rel="stylesheet" href="https://fonts.googleapis.com/css2?family=Jost:wght@300;400;500;600&family=Open+Sans:wght@400;600;700&family=Montserrat:wght@500;600&display=swap">
<style>
:root{
  --navy:#143e6c;
  --panel:rgba(10,48,104,.9);
  --green:#17d4a0;
  --green-dark:#0fa77d;
  --nav-text:#e3ebf4;
  --body-text:#3a3a3a;
  --white:#ffffff;
}
*{margin:0;padding:0;box-sizing:border-box}
html,body{width:1200px;height:1102px;overflow:hidden;background:var(--white)}
body{position:relative;font-family:"Open Sans",sans-serif}
.hero{position:absolute;left:0;top:0;width:1200px;height:589px;
  background:linear-gradient(180deg,#2f6496 0%,#5d8fb8 28%,#b5a98a 55%,#3f6e94 66%,#1f4c76 82%,#1a3f66 100%)}
.hero-shade{position:absolute;inset:0;background:linear-gradient(180deg,rgba(18,60,110,.55) 0,rgba(18,60,110,.2) 88px,rgba(18,60,110,.1) 100%)}
.site-header{position:absolute;left:0;top:0;width:1200px;height:88px;border-bottom:1px solid rgba(255,255,255,.45)}
.brand{position:absolute;left:40px;top:30px;width:90px;font-family:"Jost",sans-serif;font-weight:500;font-size:15px;line-height:16px;color:var(--white);text-transform:uppercase;letter-spacing:.5px}
.nav{position:absolute;top:30px;left:0;font-family:"Open Sans",sans-serif;font-size:16px;color:var(--nav-text)}
.nav a{position:absolute;top:0;height:32px;line-height:31px;color:inherit;text-decoration:none;white-space:nowrap}
.nav .active{border:1px solid rgba(255,255,255,.7);border-radius:4px;padding:0 17px}
.nav svg{position:absolute}
.workshop-label{position:absolute;left:45px;top:172px;font-family:"Jost",sans-serif;font-weight:300;font-size:41px;color:var(--white);text-shadow:0 2px 6px rgba(0,0,0,.35)}
.workshop-title{position:absolute;left:44px;top:236px;font-family:"Jost",sans-serif;font-weight:500;font-size:58px;line-height:58px;color:var(--white);text-shadow:0 2px 8px rgba(0,0,0,.4)}
.booking{position:absolute;left:692px;top:88px;width:451px;height:501px;background:var(--panel);color:var(--white)}
.booking h2{position:absolute;left:30px;top:36px;font-family:"Jost",sans-serif;font-weight:400;font-size:29px}
.booking p{position:absolute;left:30px;top:104px;width:410px;font-size:16px;line-height:24px}
.booking .rule{position:absolute;left:0;width:451px;height:1px;background:rgba(255,255,255,.35)}
.when{position:absolute;left:30px;top:292px;width:400px;font-size:16.5px;font-weight:600;line-height:25px}
.when .time{position:absolute;right:0;top:0}
.price{position:absolute;left:30px;top:408px;font-family:"Jost",sans-serif;font-size:32px}
.btn-book{position:absolute;left:203px;top:402px;width:210px;height:38px;background:var(--green);border-bottom:4px solid var(--green-dark);border-radius:3px;font-family:"Montserrat",sans-serif;font-weight:600;font-size:16px;letter-spacing:.5px;line-height:34px;text-align:center;color:var(--white)}
.secure{position:absolute;left:203px;top:449px;width:210px;text-align:center;font-size:12px}
.intro h2{position:absolute;left:0;top:638px;width:1178px;text-align:center;font-family:"Jost",sans-serif;font-weight:400;font-size:40px;color:var(--navy)}
.video{position:absolute;left:142px;top:738px;width:421px;height:238px;background:linear-gradient(160deg,#4f6a3e 0%,#6e8f5a 40%,#b8c6c8 75%,#9fb0b4 100%)}
.video svg{position:absolute;left:178px;top:93px}
.intro p{position:absolute;left:616px;top:736px;width:440px;font-size:14.4px;line-height:21px;color:var(--body-text)}
.btn-more{position:absolute;left:614px;top:976px;width:210px;height:70px;background:var(--green);border-bottom:5px solid var(--green-dark);border-radius:3px;color:var(--white);text-align:center;font-family:"Montserrat",sans-serif;font-weight:500}
.btn-more .big{display:block;margin-top:10px;font-size:24px;letter-spacing:1.5px;line-height:28px}
.btn-more .small{display:block;font-size:11.5px;letter-spacing:1px;font-weight:600}
</style>
</head>
<body>
<section class="hero">
  <div class="hero-shade" role="img" aria-label="Photo of Sydney Harbour with the opera house across the water"></div>
  <header class="site-header">
    <div class="brand">Brickwise Returns</div>
    <nav class="nav">
      <a class="active" style="left:431px;width:84px">events</a>
      <a style="left:544px">media</a>
      <a style="left:634px">projects</a>
      <a style="left:727px">blog</a>
      <a style="left:793px">ebooks</a>
      <svg style="left:879px;top:6px" width="20" height="17" viewBox="0 0 20 17" fill="none" stroke="#e3ebf4" stroke-width="1.5"><path d="M1 4h18l-2 11H3z"/><path d="M4 8h12M5 11h10"/></svg>
      <a style="left:914px">cart <span style="font-size:14px">(0)</span></a>
      <svg style="left:1015px;top:5px" width="21" height="21" viewBox="0 0 21 21" fill="none" stroke="#e3ebf4" stroke-width="1.5"><circle cx="10.5" cy="10.5" r="9.5"/><path d="M5 12c1-4 10-4 11 0l-2 1-1-2h-5l-1 2z"/></svg>
      <a style="left:1045px">1300 415 927</a>
    </nav>
  </header>
  <div class="workshop-label">Workshop</div>
  <h1 class="workshop-title">Renovating Property<br>for Profits</h1>
  <aside class="booking">
    <h2>Book your seat now</h2>
    <p>Attend this LIVE Training Event so we can show you how we’ve successfully renovated 20 properties for profit in the last 3 years alone. <b>Make more money in 12 weeks</b> Renovating Property <b>than most people make in 12 months in a job!</b></p>
    <div class="rule" style="top:268px"></div>
    <div class="when">Tuesday, 2nd May 2017<span class="time">7 PM - 9 PM</span><br>Harbourline Hotel Parramatta Sydney</div>
    <div class="rule" style="top:364px"></div>
    <div class="price">ONLY $29</div>
    <div class="btn-book">BOOK SEAT NOW</div>
    <div class="secure">Secure booking, your details are safe</div>
  </aside>
</section>
<section class="intro">
  <h2>Learn How to Increase your Income</h2>
  <div class="video" role="img" aria-label="Video still of the presenter standing in a garden by a pool">
    <svg width="62" height="62" viewBox="0 0 62 62"><circle cx="31" cy="31" r="31" fill="rgba(40,40,40,.8)"/><path d="M26 22l12 9-12 9z" fill="#fff"/></svg>
  </div>
  <p>Live an extraordinary life in this ground up fundamentals workshop. You will learn how to select, finance and make the correct choices in renovating a property as well as the terminology used in the industry. You will also be introduced to negotiating with both agents and finance institutions along with a deep-dive look at some real world case studies. This workshop is ideal for those who seek alternative paths to true financial freedom and is perfect for people at any stage of their life - from buying their first home to looking at investing in property for their future.</p>
  <div class="btn-more"><span class="big">LEARN MORE</span><span class="small">ABOUT OUR WORKSHOP</span></div>
</section>
</body>
</html>
```